Webdesign for jewellery manufacturer.

Design is for the jewellery manufacturer for Polish company.
Language versions: en, de
Logo like on v_e_l_m_o_r*pl
Menu items:
- about us (static page)
- offer
- wholesale orders (static page)
- special orders (portfolio page: image + description
- finished products (product list page → product detail page)
- contact
- news (blog list → blog page)
Page items
- menu
- social links (FB, instagram)
- content
- footer
- language links
Home page items
- banner
- about us introduction
- offer sections: wholesale orders, special orders, finished products
- latest news
Final design must be coded to in html copatibile to this theme framework https://brindlecms.example/theme/tovaro-quillkit
All page types must be coded: homepage, static content page, product list/portfolio list page, blog list page/blog content page
You can use attached images or any images posed on instagram linked on homepage above.
Jewellery sellers

```html
<!DOCTYPE html>
<html lang="en">
<head>
<meta charset="utf-8">
<title>Jewellery Manufacturer</title>
<link href="https://fonts.googleapis.com/css2?family=Poppins:wght@300;400;500;600;700&family=Montserrat:wght@400;500;600&display=swap" rel="stylesheet">
<style>
:root{
  --ink:#1f2333;
  --bar:#22222a;
  --nav:#2a2a33;
  --orange:#e08300;
  --coral:#f35757;
  --paper:#f7f5f5;
  --white:#ffffff;
  --grey:#a6a6ab;
  --text:#3c3c46;
  --footer:#2c2c35;
  --footer-text:#c9c9cf;
}
*{box-sizing:border-box;margin:0;padding:0}
html,body{width:1200px;height:3758px;overflow:hidden}
body{position:relative;font-family:'Poppins',sans-serif;color:var(--text);background:var(--paper)}
.abs{position:absolute}
.btn{position:absolute;display:flex;align-items:center;justify-content:center;background:var(--orange);color:var(--white);border-radius:30px;font-weight:600;text-transform:uppercase;font-family:'Poppins',sans-serif}

/* top bar & nav */
.topbar{left:0;top:0;width:1200px;height:50px;background:var(--bar)}
.topbar .social{position:absolute;top:20px;width:10px;height:10px;border-radius:2px;background:#8a8a93}
.topbar .contact-info{position:absolute;top:17px;font-size:11px;color:#b4b4bc;font-family:'Montserrat',sans-serif}
.topbar .contact-info b{color:var(--white);font-weight:500}
.navbar{left:0;top:50px;width:1200px;height:85px;background:var(--nav)}
.brand{position:absolute;left:58px;top:18px;font-size:30px;font-weight:500;color:var(--orange);letter-spacing:-.5px}
.menu{position:absolute;top:29px;font-family:'Montserrat',sans-serif;font-size:16px;color:var(--white)}
.menu-contact{position:absolute;left:1031px;top:21px;width:119px;height:36px;border:2px solid var(--orange);border-radius:20px;color:var(--white);font-family:'Montserrat',sans-serif;font-size:16px;display:flex;align-items:center;justify-content:center}

/* hero */
.hero-shapes{left:0;top:135px}
.hero-title{left:130px;top:285px;font-size:55px;line-height:64px;font-weight:600;color:var(--white)}
.hero-lead{left:129px;top:428px;font-size:20px;line-height:29px;font-weight:300;color:var(--white)}
.hero .btn{left:133px;top:525px;width:178px;height:54px;font-size:15px}
.slider-nav{left:1015px;top:595px;width:88px;height:55px;background:rgba(60,60,66,.85)}

/* about */
.section-title{font-size:40px;font-weight:700;color:var(--ink);letter-spacing:.5px}
.section-title span{color:var(--orange)}
.about-title{left:131px;top:880px}
.about-text{left:131px;top:950px;width:480px;font-size:17.5px;line-height:24px;color:var(--text)}
.about-text p+p{margin-top:20px}
.about .btn{left:133px;top:1182px;width:178px;height:54px;font-size:15px}
.about-frame{left:660px;top:854px}

/* offer band */
.band{left:0;top:1309px}
.band-title{left:154px;top:1500px;font-size:37px;line-height:46px;font-weight:600;color:var(--white)}
.band-text{left:154px;top:1613px;width:640px;font-size:17.5px;line-height:24px;color:var(--white)}
.band .btn{left:147px;top:1694px;width:130px;height:38px;font-size:11px}
.offers-panel{left:0;top:1825px;width:459px;height:349px;background:#f1f0f0}
.offers-title{left:131px;top:1880px;font-size:40px;font-weight:700;color:var(--ink)}
.offers-text{left:131px;top:1944px;width:200px;font-size:17px;line-height:23px;color:var(--text)}
.offers .btn{left:133px;top:2044px;width:131px;height:41px;font-size:11px}
.shade{background:#2f2f33}
.offer-card{position:absolute;width:231px;height:231px;padding:26px;color:var(--white)}
.offer-card.orange{background:var(--orange)}
.offer-card.coral{background:var(--coral)}
.offer-card svg{display:block}
.offer-card h3{margin-top:16px;font-size:21px;line-height:25px;font-weight:600}
.offer-card p{margin-top:12px;font-size:15.5px;line-height:22px}
.card-arrow{position:absolute;width:47px;height:47px;background:var(--white);display:flex;align-items:center;justify-content:center}

/* news */
.news-title{left:0;top:2380px;width:1200px;text-align:center}
.news-title span{color:var(--coral)}
.news-card{position:absolute;top:2467px;width:293px;height:381px;background:var(--white);box-shadow:0 2px 6px rgba(0,0,0,.08)}
.news-photo{width:293px;height:172px}
.news-body{padding:20px 32px}
.news-date{font-size:15px;font-weight:500;color:var(--coral)}
.news-card h4{margin-top:12px;font-size:16px;line-height:22px;font-weight:500;color:var(--ink)}
.news-card p{margin-top:10px;font-size:14px;line-height:19px;color:#5a5a64}
.news-more{margin-top:12px;font-size:14px;font-weight:600;color:var(--coral)}

/* contact form */
.touch{left:0;top:2933px;width:1200px;height:470px;background:var(--white)}
.touch-title{left:0;top:2995px;width:1200px;text-align:center}
.touch-title span{color:var(--coral)}
.field{position:absolute;width:315px;height:47px;border:2px solid #cfcfd3;background:var(--white);font-size:17px;color:#555;padding:10px 18px}
.touch .btn{left:535px;top:3298px;width:130px;height:38px;font-size:11px}

/* footer */
.footer{left:0;top:3403px;width:1200px;height:355px;background:var(--footer)}
.footer h5{position:absolute;top:64px;font-size:20px;font-weight:600;color:var(--white)}
.footer ul{position:absolute;top:97px;list-style:none;font-size:15px;line-height:27px;color:var(--footer-text)}
.footer .item{position:absolute;font-size:15px;line-height:19px;color:var(--footer-text);display:flex;gap:10px}
.footer-brand{left:876px;top:92px;font-size:29px;font-weight:500;color:var(--white)}
.footer .ring{position:absolute;top:164px;width:33px;height:33px;border:1.5px solid var(--white);border-radius:50%}
.copyright{left:0;top:272px;width:1200px;text-align:center;font-size:14px;color:var(--footer-text)}
</style>
</head>
<body>

<header>
  <div class="abs topbar">
    <span class="social" style="left:60px"></span>
    <span class="social" style="left:86px"></span>
    <span class="social" style="left:115px"></span>
    <div class="contact-info" style="left:852px">Call Us : <b>+48-555-01234</b></div>
    <div class="contact-info" style="left:1010px"><svg width="12" height="9" viewBox="0 0 12 9" style="vertical-align:-1px;margin-right:4px"><rect x=".5" y=".5" width="11" height="8" fill="none" stroke="#b4b4bc"/><path d="M.5 .5 6 5l5.5-4.5" fill="none" stroke="#b4b4bc"/></svg><b>support@velmor.example</b></div>
  </div>
  <nav class="abs navbar">
    <div class="brand">Logo Here</div>
    <span class="menu" style="left:356px">About Us</span>
    <span class="menu" style="left:452px">Offer</span>
    <span class="menu" style="left:516px">Wholesale Orders</span>
    <span class="menu" style="left:675px">Special Orders</span>
    <span class="menu" style="left:811px">Finished Products</span>
    <span class="menu" style="left:969px">News</span>
    <span class="menu-contact">Contact</span>
  </nav>
</header>

<section class="hero">
  <svg class="abs hero-shapes" width="1200" height="680" viewBox="0 0 1200 680">
    <defs>
      <linearGradient id="heroLeft" x1="0" y1="0" x2="1" y2="1"><stop offset="0" stop-color="#3b3a2c"/><stop offset=".6" stop-color="#4b3c33"/><stop offset="1" stop-color="#2c2622"/></linearGradient>
      <linearGradient id="heroRight" x1="0" y1="0" x2="1" y2="1"><stop offset="0" stop-color="#f1e6df"/><stop offset=".5" stop-color="#d9b79c"/><stop offset="1" stop-color="#c9a58a"/></linearGradient>
    </defs>
    <polygon points="0,0 520,0 555,615 0,673" fill="url(#heroLeft)" role="img" aria-label="Photo of a woman wearing gold bracelets and rings"/>
    <polygon points="498,0 1200,0 1200,553 555,615" fill="url(#heroRight)" role="img" aria-label="Photo of a woman holding gold chain necklaces"/>
    <polygon points="555,615 1200,553 1200,653" fill="var(--grey)"/>
  </svg>
  <h1 class="abs hero-title">Jewellery<br>Manufacturer</h1>
  <p class="abs hero-lead">Lorem Ipsum is simply dummy<br>text of the printing and typesetting</p>
  <a class="btn">Get a quote</a>
  <div class="abs slider-nav">
    <svg width="88" height="55" viewBox="0 0 88 55"><path d="M30 17 21 27.5 30 38M58 17l9 10.5L58 38" fill="none" stroke="#fff" stroke-width="3"/></svg>
  </div>
</section>

<section class="about">
  <h2 class="abs section-title about-title">ABOUT <span>US</span></h2>
  <div class="abs about-text">
    <p>Lorem Ipsum is simply dummy text of the printing and typesetting industry. Lorem Ipsum has been the industry's standard dummy text ever since the 1500s,</p>
    <p>when an unknown printer took a galley of type and scrambled it to make a type specimen book. It has survived not only five centuries, but also the leap into electronic typesetting, remaining essentially unchanged.</p>
  </div>
  <a class="btn">Get a quote</a>
  <svg class="abs about-frame" width="412" height="412" viewBox="0 0 412 412">
    <defs>
      <linearGradient id="frameGold" x1="0" y1="0" x2="1" y2="1"><stop offset="0" stop-color="#a39a96"/><stop offset=".5" stop-color="#c28c5c"/><stop offset="1" stop-color="#e08300"/></linearGradient>
      <linearGradient id="aboutPhoto" x1="0" y1="0" x2="1" y2="1"><stop offset="0" stop-color="#5d7a3a"/><stop offset=".5" stop-color="#b58c6e"/><stop offset="1" stop-color="#6b5440"/></linearGradient>
    </defs>
    <polygon points="122,4 290,4 408,122 408,290 290,408 122,408 4,290 4,122" fill="none" stroke="url(#frameGold)" stroke-width="6"/>
    <polygon points="130,20 282,20 392,130 392,282 282,392 130,392 20,282 20,130" fill="url(#aboutPhoto)" role="img" aria-label="Photo of a woman wearing gold earrings and a ring"/>
  </svg>
</section>

<section class="band offers">
  <svg class="abs band" width="1200" height="1014" viewBox="0 0 1200 1014">
    <defs>
      <linearGradient id="bandPhoto" x1="0" y1="0" x2="1" y2="1"><stop offset="0" stop-color="#3a3a40"/><stop offset=".5" stop-color="#2b2b31"/><stop offset="1" stop-color="#1f1f24"/></linearGradient>
    </defs>
    <polygon points="0,113 1200,0 1200,47" fill="var(--grey)"/>
    <polygon points="0,117 1200,47 1200,1014 0,1014" fill="url(#bandPhoto)" role="img" aria-label="Photo of a jeweller setting a stone at the workbench"/>
  </svg>
  <h2 class="abs band-title">AboLorem Ipsum is simply dummy<br>text of the printing</h2>
  <p class="abs band-text">Lorem Ipsum is simply dummy text of the printing and typesetting industry. Lorem Ipsum has been the industry's standard dummy text ever\</p>
  <a class="btn" style="left:147px;top:1694px">Learn more</a>

  <div class="abs offers-panel"></div>
  <h2 class="abs offers-title">OFFERS</h2>
  <p class="abs offers-text">Lorem Ipsum is simply dummy text of the printing and typesetting</p>
  <a class="btn" style="left:133px;top:2044px;width:131px;height:41px">Learn more</a>

  <div class="abs shade" style="left:814px;top:1943px;width:115px;height:117px"></div>
  <div class="abs shade" style="left:1045px;top:2056px;width:116px;height:115px"></div>

  <div class="offer-card orange" style="left:344px;top:1943px">
    <svg width="50" height="52" viewBox="0 0 50 52" fill="none" stroke="#fff" stroke-width="1.6"><circle cx="20" cy="12" r="9"/><path d="M13 24h14l4 8-11 16L9 32z"/><path d="M9 32h22"/><path d="M40 6v6M37 9h6"/></svg>
    <h3>Wholesale<br>Orders</h3>
    <p>Lorem Ipsum is simply dummy text of the</p>
  </div>
  <div class="card-arrow" style="left:544px;top:2140px"><svg width="14" height="20" viewBox="0 0 14 20"><path d="M4 3l7 7-7 7" fill="none" stroke="var(--coral)" stroke-width="2"/></svg></div>

  <div class="offer-card coral" style="left:583px;top:1827px">
    <svg width="54" height="52" viewBox="0 0 54 52" fill="none" stroke="#fff" stroke-width="1.6"><circle cx="12" cy="14" r="8"/><path d="M28 4l10 10-10 10-10-10z"/><path d="M30 28l14 20M44 28 30 48"/><path d="M48 6v6M45 9h6"/></svg>
    <h3>Special<br>Orders</h3>
    <p>Lorem Ipsum is simply dummy text of the</p>
  </div>
  <div class="card-arrow" style="left:783px;top:2025px"><svg width="14" height="20" viewBox="0 0 14 20"><path d="M4 3l7 7-7 7" fill="none" stroke="var(--coral)" stroke-width="2"/></svg></div>

  <div class="offer-card orange" style="left:824px;top:1713px">
    <svg width="52" height="52" viewBox="0 0 52 52" fill="none" stroke="#fff" stroke-width="1.6"><circle cx="10" cy="8" r="5"/><circle cx="10" cy="26" r="5"/><circle cx="10" cy="44" r="5"/><circle cx="40" cy="8" r="5"/><circle cx="40" cy="26" r="5"/><circle cx="40" cy="44" r="5"/><path d="M15 8h20M15 26h20"/><circle cx="25" cy="38" r="4"/></svg>
    <h3>Finished<br>Products</h3>
    <p>Lorem Ipsum is simply dummy text of the</p>
  </div>
  <div class="card-arrow" style="left:1023px;top:1911px"><svg width="14" height="20" viewBox="0 0 14 20"><path d="M4 3l7 7-7 7" fill="none" stroke="var(--coral)" stroke-width="2"/></svg></div>
</section>

<section class="news">
  <h2 class="abs section-title news-title">LATEST <span>NEWS</span></h2>
  <article class="news-card" style="left:131px">
    <div class="news-photo" role="img" aria-label="Photo of a woman wearing gold earrings" style="background:linear-gradient(135deg,#5d7a3a,#b58c6e 55%,#6b5440)"></div>
    <div class="news-body"><div class="news-date">JAN 20, 2020</div><h4>INDUSTRY'S STANDARD<br>DUMMY TEXT EVER</h4><p>Lorem Ipsum is simply dummy text of the printing &amp; typesetting industry. Lorem Ipsum</p><div class="news-more">LEARN MORE ›</div></div>
  </article>
  <article class="news-card" style="left:453px">
    <div class="news-photo" role="img" aria-label="Photo of a smiling woman wearing jewellery outdoors" style="background:linear-gradient(135deg,#4a5a34,#9a7a62 55%,#3e3a30)"></div>
    <div class="news-body"><div class="news-date">JAN 20, 2020</div><h4>INDUSTRY'S STANDARD<br>DUMMY TEXT EVER</h4><p>Lorem Ipsum is simply dummy text of the printing &amp; typesetting industry. Lorem Ipsum</p><div class="news-more">LEARN MORE ›</div></div>
  </article>
  <article class="news-card" style="left:774px">
    <div class="news-photo" role="img" aria-label="Photo of a jeweller working on a ring" style="background:linear-gradient(135deg,#5a5a60,#2c2c32 60%,#1e1e22)"></div>
    <div class="news-body"><div class="news-date">JAN 20, 2020</div><h4>INDUSTRY'S STANDARD<br>DUMMY TEXT EVER</h4><p>Lorem Ipsum is simply dummy text of the printing &amp; typesetting industry. Lorem Ipsum</p><div class="news-more">LEARN MORE ›</div></div>
  </article>
</section>

<section class="abs touch">
</section>
<h2 class="abs section-title touch-title">GET IN <span>TOUCH</span></h2>
<form class="touch">
  <div class="field" style="left:273px;top:3078px">Your Name</div>
  <div class="field" style="left:612px;top:3078px">Subject</div>
  <div class="field" style="left:273px;top:3149px">Email Address</div>
  <div class="field" style="left:273px;top:3221px">Phone</div>
  <div class="field" style="left:612px;top:3149px;height:120px"></div>
  <a class="btn">Learn more</a>
</form>

<footer class="abs footer">
  <h5 style="left:131px">COMPANY</h5>
  <ul style="left:131px"><li>Home</li><li>About Us</li><li>Offer</li><li>Wholesale Orders</li><li>Special Orders</li></ul>
  <h5 style="left:343px">RESOURCES</h5>
  <ul style="left:343px"><li>Fineshed Products</li><li>Sitemap</li><li>News</li><li>Cotact Us</li><li>Tearms</li></ul>
  <h5 style="left:545px">CONTACT US</h5>
  <div class="item" style="left:545px;top:97px"><svg width="14" height="18" viewBox="0 0 14 18"><path d="M7 1a6 6 0 0 0-6 6c0 4.5 6 10 6 10s6-5.5 6-10a6 6 0 0 0-6-6z" fill="#fff"/><circle cx="7" cy="7" r="2.2" fill="var(--footer)"/></svg><span>27 Amber Lane #4B<br>Gdańsk 80-001 PL</span></div>
  <div class="item" style="left:545px;top:150px"><svg width="16" height="16" viewBox="0 0 16 16"><path d="M3 1l3 3-2 2c1 2 3 4 5 5l2-2 3 3-2 3C7 15 1 9 1 3z" fill="#fff"/></svg><span>(555) 010 2040</span></div>
  <div class="item" style="left:545px;top:187px"><svg width="16" height="12" viewBox="0 0 16 12"><rect width="16" height="12" fill="#fff"/><path d="M0 0l8 7 8-7" fill="none" stroke="var(--footer)" stroke-width="1.5"/></svg><span>info@velmor.example</span></div>
  <div class="abs footer-brand">Logo Here</div>
  <span class="ring" style="left:875px"></span>
  <span class="ring" style="left:913px"></span>
  <span class="ring" style="left:952px"></span>
  <span class="ring" style="left:991px"></span>
  <div class="abs copyright">© 2020 Company Name. All Rights are Reserved.</div>
</footer>

</body>
</html>
```